Business Card for Orvane Parts Wholesale supplier

Hi There! I need a new business card for our company. We are specialized in selling Orvane parts, mostly we sell new LCD screens for Telvox and Slatrons. I would like to see that back in the design.

You can find the colors and logo's on our website: www.dorvak-example.nl

Industry/Entity Type

Business

Contact Information for Business Card

My Details:
Lars Vintorp

Phone: 0031612873406
E-mail: Lars@dorvak-example.nl

Slogan: "Because Quality Matters"

Font styles to use
Sans Serif

Colors

Designer to choose colors to be used in the design.

Requirements
Must have
• A Black backside with the Dorvak logo on it. The front side should be clean with only my contact details.
• But I'm also open for something really different or awesome!
Nice to have
• Remember that we are in the parts & repairing industry, So i'll be handing those business cards mainly to repair companies. Maybe you can do something with that thought :)

```html
<!DOCTYPE html>
<html lang="en">
<head>
<meta charset="utf-8">
<title>Dorvak Business Card</title>
<link href="https://fonts.googleapis.com/css2?family=Exo+2:wght@400;600;700&display=swap" rel="stylesheet">
<style>
  :root {
    --stage: #2b2b2b;
    --card-black: #050505;
    --card-white: #ffffff;
    --ink: #1c1c1c;
    --orange: #f07623;
    --rule: #8a8a8a;
    --band: #ffffff;
  }
  * { margin: 0; padding: 0; box-sizing: border-box; }
  html, body { width: 1200px; height: 1000px; overflow: hidden; }
  body {
    position: relative;
    background: var(--stage);
    font-family: "Exo 2", sans-serif;
    color: var(--ink);
  }
  .card {
    position: absolute;
    left: 320px;
    width: 560px;
    height: 320px;
  }
  .card-back { top: 50px; background: var(--card-black); }
  .card-front { top: 420px; background: var(--card-white); }

  .wordmark {
    display: flex;
    align-items: center;
    gap: 14px;
    font-family: "Exo 2", sans-serif;
    font-weight: 700;
    letter-spacing: 1px;
    line-height: 1;
  }
  .wordmark-dot {
    display: block;
    border-radius: 50%;
    background: var(--orange);
  }
  .card-back .wordmark {
    position: absolute;
    left: 50%; top: 50%;
    transform: translate(-50%, -50%);
    color: #ffffff;
    font-size: 72px;
  }
  .card-back .wordmark-dot { width: 64px; height: 64px; }

  .card-front .wordmark {
    position: absolute;
    right: 36px; top: 34px;
    color: var(--ink);
    font-size: 58px;
  }
  .card-front .wordmark-dot { width: 52px; height: 52px; }

  .holder {
    position: absolute;
    left: 34px; top: 150px;
  }
  .holder-name {
    font-size: 19px;
    font-weight: 700;
    letter-spacing: 0.5px;
    text-transform: uppercase;
    color: var(--ink);
  }
  .holder-role {
    font-size: 15px;
    font-weight: 600;
    color: var(--orange);
  }
  .divider {
    position: absolute;
    left: 160px; right: 34px;
    top: 188px;
    height: 1px;
    background: var(--rule);
  }
  .contacts {
    position: absolute;
    left: 34px; top: 204px;
    list-style: none;
    font-size: 14px;
    line-height: 20px;
    color: var(--ink);
  }
  .contacts li { display: flex; align-items: center; gap: 8px; }
  .contacts svg { width: 12px; height: 12px; flex: none; }
  .accent { color: var(--orange); }
  .slogan {
    position: absolute;
    right: 34px; bottom: 30px;
    font-size: 14px;
    letter-spacing: 0.8px;
    color: var(--ink);
  }

  .brand-band {
    position: absolute;
    left: 0; top: 855px;
    width: 1200px; height: 145px;
    background: var(--band);
    display: flex;
    align-items: center;
    justify-content: center;
  }
  .brand-band .wordmark { color: #000000; font-size: 62px; }
  .brand-band .wordmark-dot { width: 56px; height: 56px; }
</style>
</head>
<body>

  <section class="card card-back" aria-label="Card back">
    <div class="wordmark"><span class="wordmark-dot"></span>dorvak</div>
  </section>

  <section class="card card-front" aria-label="Card front">
    <div class="wordmark"><span class="wordmark-dot"></span>dorvak</div>

    <div class="holder">
      <p class="holder-name">Lars Vintorp</p>
      <p class="holder-role">CEO and Fonuder</p>
    </div>
    <div class="divider"></div>

    <ul class="contacts">
      <li>
        <svg viewBox="0 0 12 12" aria-hidden="true"><path d="M2.5 1 L4.5 1 L5.2 3.5 L4 4.5 Q5 7 7.5 8 L8.5 6.8 L11 7.5 L11 9.5 Q11 11 9.5 11 Q1 10.5 1 2.5 Q1 1 2.5 1 Z" fill="var(--orange)"/></svg>
        0031612873406
      </li>
      <li>
        <svg viewBox="0 0 12 12" aria-hidden="true"><rect x="0.5" y="2" width="11" height="8" fill="var(--orange)"/><path d="M0.5 2 L6 6.5 L11.5 2" fill="none" stroke="#ffffff" stroke-width="1"/></svg>
        Lars@dorvak-example.nl
      </li>
      <li>
        <svg viewBox="0 0 12 12" aria-hidden="true"><circle cx="5" cy="5" r="3.5" fill="none" stroke="var(--orange)" stroke-width="1.6"/><path d="M7.5 7.5 L11 11" stroke="var(--orange)" stroke-width="1.8"/></svg>
        www.<span class="accent">dorvak-example</span>.nl
      </li>
    </ul>

    <p class="slogan">Because Quality Matters</p>
  </section>

  <footer class="brand-band">
    <div class="wordmark"><span class="wordmark-dot"></span>dorvak</div>
  </footer>

</body>
</html>
```